Unique & Creative Business Card for Lumavessence

Would you please create a unique design that is soft and appealing to people who seek to raise vibrational energy for themselves, for animals (domestic or wild), or for the environment.

Optional: Elements could include, landscapes, wild animals, feathers, vibrational patterns, the elements (Earth, water, fire, air and space). Images that are calming.

With Thanks!

Target Market(s)

People and businesses who are into the environment, animal welfare, alternative health.

Contact Information for Business Card

Moira Bell
Energist
mb@lumavessence.example
lumavessence.example

Requirements
Must have
• Lumavessence logo (attached)
Symbols that represent our main services: Natural environment, animal, human and energy.
Our strapline ‘Achieving Vibrational Equilibrium’
Nice to have
• Clear and easy to read
Colours based on nature/soft colours

```html
<!DOCTYPE html>
<html lang="en">
<head>
<meta charset="utf-8">
<title>Lumavessence Business Card</title>
<link rel="stylesheet" href="https://fonts.googleapis.com/css2?family=Oswald:wght@500&family=Work+Sans:wght@400;500&display=swap">
<style>
  :root {
    --page-bg: #2b2b2d;
    --card-blue: #2c4a8e;
    --card-blue-light: #3a5a9e;
    --sky-top: #8a8f95;
    --sky-warm: #9c8478;
    --forest-dark: #2c4a4f;
    --forest-mid: #3f6468;
    --water: #5a6d70;
    --ink-light: #ffffff;
    --ink-soft: rgba(255,255,255,0.88);
  }
  * { box-sizing: border-box; margin: 0; padding: 0; }
  html, body {
    width: 1200px; height: 930px; overflow: hidden;
    background: var(--page-bg);
    font-family: "Work Sans", Arial, sans-serif;
  }
  .canvas { position: relative; width: 1200px; height: 930px; }
  .card {
    position: absolute; width: 560px; height: 320px;
    border-radius: 18px; overflow: hidden;
    box-shadow: 0 18px 40px rgba(0,0,0,0.45);
  }
  .card-front { left: 70px; top: 110px; }
  .card-back { left: 570px; top: 500px; background: linear-gradient(120deg, var(--card-blue) 0%, var(--card-blue-light) 55%, var(--card-blue) 100%); }

  .landscape {
    position: absolute; inset: 0;
    background:
      linear-gradient(180deg, transparent 40%, var(--forest-mid) 62%, var(--forest-dark) 85%, var(--water) 100%),
      linear-gradient(180deg, var(--sky-top) 0%, var(--sky-warm) 45%, var(--forest-mid) 70%);
  }
  .brand {
    position: absolute; left: 250px; top: 110px;
    display: flex; align-items: center; gap: 12px;
  }
  .brand-dot {
    width: 26px; height: 26px; border-radius: 50%;
    border: 2px solid var(--ink-light);
  }
  .brand-name {
    font-size: 26px; font-weight: 500; color: var(--ink-light);
    letter-spacing: 0.04em;
  }
  .services {
    position: absolute; left: 36px; bottom: 34px;
    color: var(--ink-light); font-size: 15px; line-height: 1.4;
  }

  .identity {
    position: absolute; left: 60px; top: 128px;
    text-align: right; width: 220px;
  }
  .person-name {
    font-family: "Oswald", "Arial Narrow", sans-serif;
    font-size: 40px; font-weight: 500; color: var(--ink-light);
    letter-spacing: 0.01em; line-height: 1;
  }
  .person-role { color: var(--ink-soft); font-size: 17px; margin-top: 4px; }
  .divider {
    position: absolute; left: 300px; top: 112px;
    width: 1px; height: 96px; background: rgba(255,255,255,0.6);
  }
  .contacts {
    position: absolute; left: 318px; top: 122px;
    list-style: none; color: var(--ink-light); font-size: 15px;
  }
  .contacts li { display: flex; align-items: center; gap: 7px; line-height: 25px; }
  .contacts svg { width: 12px; height: 12px; flex: none; }
</style>
</head>
<body>
<main class="canvas">
  <section class="card card-front">
    <div class="landscape" role="img" aria-label="Calm mountain forest landscape with misty peaks and a river"></div>
    <div class="brand">
      <span class="brand-dot"></span>
      <span class="brand-name">Lumavessence</span>
    </div>
    <p class="services">Natural environment, animal, human and energy.<br>Our strapline ‘Achieving Vibrational Equilibrium</p>
  </section>

  <section class="card card-back">
    <div class="identity">
      <h1 class="person-name">MOIRA BELL</h1>
      <p class="person-role">Energist</p>
    </div>
    <span class="divider"></span>
    <ul class="contacts">
      <li>
        <svg viewBox="0 0 24 24" fill="#fff"><path d="M6.6 10.8a15 15 0 0 0 6.6 6.6l2.2-2.2a1 1 0 0 1 1-.25 11.4 11.4 0 0 0 3.6.57 1 1 0 0 1 1 1V20a1 1 0 0 1-1 1A17 17 0 0 1 3 4a1 1 0 0 1 1-1h3.5a1 1 0 0 1 1 1c0 1.25.2 2.45.57 3.57a1 1 0 0 1-.25 1z"/></svg>
        06.41.73.19.82
      </li>
      <li>
        <svg viewBox="0 0 24 24" fill="none" stroke="#fff" stroke-width="2.4"><rect x="3" y="5" width="18" height="14" rx="1"/><path d="M3 6l9 7 9-7"/></svg>
        mb@lumavessence.example
      </li>
      <li>
        <svg viewBox="0 0 24 24" fill="none" stroke="#fff" stroke-width="2"><circle cx="12" cy="12" r="9"/><path d="M3 12h18M12 3c3 3 3 15 0 18M12 3c-3 3-3 15 0 18"/></svg>
        www.lumavessence.example
      </li>
    </ul>
  </section>
</main>
</body>
</html>
```